BrookvaleTech Website Design

To design a website for BrookvaleTech, a software development company. The website should reflect the branding of our company, which is Smart, Beautiful, and Sophisticated. The existing website is www.brookvaletech.com.sg

```html
<!DOCTYPE html>
<html lang="en">
<head>
<meta charset="utf-8">
<title>BrookvaleTech</title>
<link rel="stylesheet" href="https://fonts.googleapis.com/css2?family=Open+Sans:wght@400;600;700&display=swap">
<style>
:root{
  --blue:#1a6fa8;
  --blue-dark:#0f5a8c;
  --nav-top:#0d6aa3;
  --nav-bottom:#00466e;
  --nav-active:#033a5b;
  --register:#1a8ac0;
  --login:#555;
  --text:#666;
  --text-dark:#333;
  --muted:#8a8a8a;
  --panel:#f5f5f5;
  --footer:#efefef;
  --bar:#222;
  --rule:#dedede;
}
*{box-sizing:border-box;margin:0;padding:0}
html,body{width:1200px;height:2296px;overflow:hidden}
body{font-family:"Open Sans",Arial,sans-serif;color:var(--text);background:#fff;position:relative}
.wrap{position:relative;width:1000px;margin:0 auto;height:100%}
section,header,footer,nav{position:relative;width:1200px}

/* header */
.site-header{height:104px;background:#fff}
.brand{position:absolute;left:0;top:20px;display:flex;align-items:center;gap:10px}
.brand-dot{width:58px;height:58px;border-radius:50%;background:var(--blue-dark)}
.brand-name{font-size:32px;font-weight:600;color:var(--blue);letter-spacing:-.3px}
.search{position:absolute;left:681px;top:29px;width:153px;height:32px;border:1px solid #ccc;border-radius:3px;background:#fff;font-size:13px;color:#999;padding:7px 0 0 24px}
.search svg{position:absolute;right:6px;top:6px}
.search::after{content:"";position:absolute;right:28px;top:0;bottom:0;border-left:1px solid #ddd}
.btn{position:absolute;top:29px;height:32px;border-radius:3px;color:#fff;font-size:13px;font-weight:600;text-align:center;line-height:32px}
.btn-register{left:843px;width:80px;background:var(--register)}
.btn-login{left:932px;width:68px;background:var(--login)}

/* nav */
.main-nav{height:51px;background:linear-gradient(var(--nav-top),var(--nav-bottom))}
.main-nav ul{list-style:none;display:flex;height:51px}
.main-nav li{color:#fff;font-size:15px;font-weight:600;line-height:51px;text-align:center}
.main-nav li.active{background:var(--nav-active)}

/* hero */
.hero{height:500px;background:radial-gradient(ellipse at 40% 55%,#f4f4f4 0%,#dcdcdc 75%)}
.hero-art{position:absolute;left:60px;top:0;width:640px;height:500px;background:radial-gradient(ellipse at 45% 55%,#fff5e6 0%,#e9e6ea 35%,rgba(220,220,220,0) 70%)}
.hero-copy{position:absolute;left:632px;top:150px;width:330px}
.hero-copy h1{font-size:27px;line-height:31px;font-weight:600;color:var(--blue-dark)}
.hero-copy p{margin-top:14px;font-size:14px;line-height:21px;color:var(--text-dark)}
.hero-cta{display:inline-block;margin-top:14px;width:146px;height:39px;line-height:39px;text-align:center;background:#404040;color:#fff;font-size:16px;border-radius:3px}
.hero-dots{position:absolute;left:451px;top:457px;width:100px;height:24px;border-radius:12px;background:#9a9a9a;display:flex;justify-content:center;align-items:center;gap:10px}
.hero-dots span{width:10px;height:10px;border-radius:50%;background:#fff}
.hero-dots span.current{background:#9a9a9a;border:2px solid #fff}

/* intro */
.intro{height:146px;border-bottom:1px solid var(--rule)}
.intro p{position:absolute;left:30px;right:30px;top:33px;text-align:center;font-size:15px;line-height:27px;color:var(--text)}

/* features */
.features{height:509px;background:var(--panel);border-bottom:1px solid var(--rule)}
.feature{position:absolute;width:300px;text-align:center}
.feature svg{display:block;margin:0 auto}
.feature h3{font-size:24px;font-weight:600;color:var(--blue);margin-top:10px;line-height:30px}
.feature p{font-size:13.5px;line-height:20px;color:var(--muted);margin-top:6px}

/* as seen on */
.seen-on{height:164px;border-bottom:1px solid var(--rule)}
.seen-on h4{position:absolute;left:0;right:0;top:38px;text-align:center;font-size:15px;font-weight:400;color:#777}
.partner-row{position:absolute;left:-15px;right:-15px;top:76px;display:flex;justify-content:space-between;align-items:center}
.partner{font-size:22px;font-weight:600;color:#777}

/* works */
.works{height:351px;background:var(--panel);border-bottom:1px solid var(--rule)}
.works h2{position:absolute;left:0;right:0;top:28px;text-align:center;font-size:24px;font-weight:600;color:var(--blue)}
.work{position:absolute;top:86px;width:312px;text-align:center}
.work h5{font-size:17px;font-weight:600;color:var(--text-dark);line-height:22px}
.work-shot{margin-top:12px;width:312px;height:189px}
.shot-browser{background:linear-gradient(160deg,#e7edf4 0%,#b7c7d8 45%,#3c5a8a 80%,#1f3460 100%)}
.shot-pencils{background:linear-gradient(135deg,#e2e4e6 0%,#c9ccd1 45%,#e0a640 60%,#b8c6d4 80%,#d8dbde 100%)}
.shot-keys{background:linear-gradient(150deg,#ececec 0%,#dcdcdc 55%,#9fc45a 75%,#e5e5e5 100%)}

/* testimonial */
.testimonial{height:153px}
.testimonial blockquote{position:absolute;left:0;right:0;top:30px;text-align:center;font-size:20px;line-height:28px;color:var(--text-dark)}
.testimonial .mark{font-size:26px;font-weight:700;color:#444;vertical-align:-4px}
.testimonial cite{position:absolute;left:0;right:0;top:96px;text-align:center;font-style:normal;font-size:16px;color:var(--register)}

/* footer */
.site-footer{height:251px;background:var(--footer);border-top:1px solid var(--rule)}
.footer-col h4{position:absolute;top:18px;font-size:18px;font-weight:400;color:var(--text-dark)}
.quick-links{position:absolute;top:62px;list-style:none}
.quick-links li{font-size:13px;line-height:29.4px;color:var(--muted)}
.quick-links li::before{content:"•";margin-right:8px;font-size:10px}
.divider{position:absolute;top:18px;height:206px;border-left:1px solid #d4d4d4}
.field{position:absolute;left:528px;width:226px;height:29px;border:1px solid #ccc;background:#fff;font-size:12px;color:var(--text-dark);padding:6px 0 0 16px}
.submit{position:absolute;left:684px;top:148px;width:70px;height:29px;background:#595959;color:#fff;font-size:13px;font-weight:600;text-align:center;line-height:29px}
.social{position:absolute;left:805px;display:flex;align-items:center;font-size:12px;color:var(--muted)}
.social-badge{width:28px;height:28px;border-radius:3px;margin-right:10px}
.social strong{font-size:16px;font-weight:400;margin-left:8px}
.bottom-bar{height:67px;background:var(--bar);color:#aaa;font-size:12.5px;text-align:center;line-height:67px}
</style>
</head>
<body>

<header class="site-header">
  <div class="wrap">
    <div class="brand"><span class="brand-dot"></span><span class="brand-name">BrookvaleTech</span></div>
    <div class="search">Search
      <svg width="18" height="18" viewBox="0 0 18 18"><circle cx="7.5" cy="7.5" r="5.5" fill="none" stroke="#888" stroke-width="2"/><line x1="11.5" y1="11.5" x2="16" y2="16" stroke="#888" stroke-width="2.4"/></svg>
    </div>
    <div class="btn btn-register">REGISTER</div>
    <div class="btn btn-login">LOG IN</div>
  </div>
</header>

<nav class="main-nav">
  <div class="wrap">
    <ul>
      <li class="active" style="width:105px">HOME</li>
      <li style="width:165px">ABOUT US</li>
      <li style="width:150px">SERVICES</li>
      <li style="width:145px">WORKS</li>
      <li style="width:140px">BLOG</li>
      <li style="width:120px">FAQ</li>
      <li style="width:175px">CONTACT US</li>
    </ul>
  </div>
</nav>

<section class="hero">
  <div class="hero-art" role="img" aria-label="Tablet computer leaning forward with colourful app icons streaming out of its screen"></div>
  <div class="wrap">
    <div class="hero-copy">
      <h1>Maecenas sed lacus ac nisi pellentesque</h1>
      <p>Integer bibendum, diam et convallis euismod, est tortor rhoncus metus, eget ultricies purus odio at mi eros est, non fringilla lectus.</p>
      <div class="hero-cta">Contact us Now</div>
    </div>
  </div>
  <div class="hero-dots" style="left:551px"><span class="current"></span><span></span><span></span><span></span></div>
</section>

<section class="intro">
  <div class="wrap">
    <p>BrookvaleTech Pte Ltd is a member company of the HarbourGroup. HarbourGroup was founded by the late Mr Tan Wei Ming in 1970. HarbourGroup consists of Marina Emporium Pte Ltd, Marina Movie Pte Ltd, Marina Movie Distributions Pte Ltd, Marina Investment Pte Ltd, and BrookvaleTech Pte Ltd. BrookvaleTech specializes in development of smart media content, software and technology.</p>
  </div>
</section>

<section class="features">
  <div class="wrap">
    <div class="feature" style="left:15px;top:34px">
      <svg width="80" height="84" viewBox="0 0 80 84"><path d="M28 4h24l-8 12h-8z" fill="var(--blue)"/><rect x="30" y="16" width="20" height="6" rx="2" fill="var(--blue)"/><path d="M30 22C10 32 2 50 4 64c2 14 16 18 36 18s34-4 36-18c2-14-6-32-26-42z" fill="var(--blue)"/><text x="40" y="68" text-anchor="middle" font-family="Open Sans, sans-serif" font-weight="700" font-size="32" fill="#fff">$</text></svg>
      <h3>Affordable Price</h3>
      <p>Maecenas dapibus massa ut sem fermentum tristique. Nunc dolor augue, pulvinar vitae mattis id, blandit non nunc.</p>
    </div>
    <div class="feature" style="left:349px;top:34px">
      <svg width="84" height="84" viewBox="0 0 84 84"><path d="M60 4a20 20 0 0 0-19 26L6 65a8 8 0 0 0 13 13l35-35a20 20 0 0 0 26-19l-12 8-10-4-4-10z" fill="var(--blue)"/><circle cx="13" cy="71" r="3" fill="#fff"/></svg>
      <h3>Easy Customization</h3>
      <p>Maecenas dapibus massa ut sem fermentum tristique. Nunc dolor augue, pulvinar vitae mattis id, blandit non nunc.</p>
    </div>
    <div class="feature" style="left:685px;top:34px">
      <svg width="100" height="84" viewBox="0 0 100 84"><rect x="24" y="4" width="72" height="52" rx="3" fill="none" stroke="var(--blue)" stroke-width="6"/><rect x="48" y="56" width="24" height="12" fill="var(--blue)"/><rect x="40" y="68" width="40" height="5" fill="var(--blue)"/><rect x="12" y="24" width="32" height="58" rx="3" fill="#fff" stroke="var(--blue)" stroke-width="5"/><rect x="2" y="46" width="20" height="36" rx="3" fill="#fff" stroke="var(--blue)" stroke-width="4"/></svg>
      <h3>Responsive Desings</h3>
      <p>Maecenas dapibus massa ut sem fermentum tristique. Nunc dolor augue, pulvinar vitae mattis id, blandit non nunc.</p>
    </div>

    <div class="feature" style="left:15px;top:278px">
      <svg width="80" height="80" viewBox="0 0 80 80"><circle cx="40" cy="40" r="38" fill="var(--blue)"/><path d="M40 14L18 38h14v24h16V38h14z" fill="#fff"/></svg>
      <h3>Regular Updates</h3>
      <p>Maecenas dapibus massa ut sem fermentum tristique. Nunc dolor augue, pulvinar vitae mattis id, blandit non nunc.</p>
    </div>
    <div class="feature" style="left:349px;top:278px">
      <svg width="80" height="80" viewBox="0 0 80 80"><path d="M12 42a28 28 0 0 1 56 0" fill="none" stroke="var(--blue)" stroke-width="6"/><rect x="6" y="38" width="16" height="26" rx="6" fill="var(--blue)"/><rect x="58" y="38" width="16" height="26" rx="6" fill="var(--blue)"/><path d="M66 62c0 10-12 14-24 14" fill="none" stroke="var(--blue)" stroke-width="4"/><rect x="30" y="71" width="14" height="8" rx="3" fill="var(--blue)"/></svg>
      <h3>Cusotmer Support</h3>
      <p>Maecenas dapibus massa ut sem fermentum tristique. Nunc dolor augue, pulvinar vitae mattis id, blandit non nunc.</p>
    </div>
    <div class="feature" style="left:685px;top:278px">
      <svg width="84" height="80" viewBox="0 0 84 80"><circle cx="20" cy="30" r="10" fill="var(--blue)"/><circle cx="64" cy="30" r="10" fill="var(--blue)"/><path d="M2 64c0-14 8-20 18-20s18 6 18 20z" fill="var(--blue)"/><path d="M46 64c0-14 8-20 18-20s18 6 18 20z" fill="var(--blue)"/><circle cx="42" cy="26" r="13" fill="var(--blue)" stroke="#f5f5f5" stroke-width="3"/><path d="M18 68c0-18 10-26 24-26s24 8 24 26z" fill="var(--blue)" stroke="#f5f5f5" stroke-width="3"/></svg>
      <h3>We’re Hiring</h3>
      <p>Maecenas dapibus massa ut sem fermentum tristique. Nunc dolor augue, pulvinar vitae mattis id, blandit non nunc.</p>
    </div>
  </div>
</section>

<section class="seen-on">
  <div class="wrap">
    <h4>As Seen On</h4>
    <div class="partner-row">
      <span class="partner">Fernmarket</span>
      <span class="partner">Quarrly</span>
      <span class="partner">Linkwise</span>
      <span class="partner">Thymera</span>
      <span class="partner">Kenzora</span>
      <span class="partner">NT</span>
      <span class="partner">Macrovolt</span>
      <span class="partner">Adeline</span>
      <span class="partner">Sorvo</span>
    </div>
  </div>
</section>

<section class="works">
  <div class="wrap">
    <h2>Our Works</h2>
    <div class="work" style="left:0">
      <h5>Maecenas sed</h5>
      <div class="work-shot shot-browser" role="img" aria-label="Close-up of a web browser address bar and navigation toolbar"></div>
    </div>
    <div class="work" style="left:344px">
      <h5>Aliquam egestas</h5>
      <div class="work-shot shot-pencils" role="img" aria-label="Pencils and drafting tools in a glass beside colour swatches"></div>
    </div>
    <div class="work" style="left:688px">
      <h5>Morbi vel</h5>
      <div class="work-shot shot-keys" role="img" aria-label="Computer keyboard with a green shopping key"></div>
    </div>
  </div>
</section>

<section class="testimonial">
  <blockquote><span class="mark">“</span>&nbsp; onec consectetur turpis sit amet lorem faucibus, et bibendum felis fermentum.<br>Maecenas dapibus massa ut sem fermentum tristique &nbsp;<span class="mark">”</span></blockquote>
  <cite>- &nbsp;Customer name, City</cite>
</section>

<footer class="site-footer">
  <div class="wrap">
    <div class="footer-col"><h4 style="left:3px">Quick Links</h4></div>
    <ul class="quick-links" style="left:3px"><li>Integer lobortis</li><li>Curabitur ac</li><li>Phasellus tellus nisl</li><li>Aenean fringilla</li><li>Vestibulum</li><li>Aliquam commodo</li></ul>
    <ul class="quick-links" style="left:172px"><li>Integer lobortis</li><li>Curabitur ac</li><li>Phasellus tellus nisl</li><li>Aenean fringilla</li><li>Vestibulum</li><li>Aliquam commodo</li></ul>
    <ul class="quick-links" style="left:350px"><li>Integer lobortis</li><li>Curabitur ac</li><li>Phasellus tellus nisl</li><li>Aenean fringilla</li><li>Vestibulum</li><li>Aliquam commodo</li></ul>
    <div class="divider" style="left:502px"></div>

    <div class="footer-col"><h4 style="left:528px">Email Signup</h4></div>
    <div class="field" style="top:65px">Name</div>
    <div class="field" style="top:108px">Email ID</div>
    <div class="submit">SUBMIT</div>
    <div class="divider" style="left:777px"></div>

    <div class="footer-col"><h4 style="left:805px">Connect with us</h4></div>
    <div class="social" style="top:63px"><span class="social-badge" style="background:#3b5a96"></span>Join with us on<strong style="color:#2b4a8a">Friendwall</strong></div>
    <div class="social" style="top:105px"><span class="social-badge" style="background:#3fa9dc"></span>Follow us on<strong style="color:#2a9bd4">Chirpline</strong></div>
    <div class="social" style="top:147px"><span class="social-badge" style="background:#1c6ea1"></span>Share on<strong style="color:#1c6ea1">Careernet</strong></div>
    <div class="social" style="top:189px"><span class="social-badge" style="background:#c4302b"></span>Watch on<strong style="color:#222">ClipStream</strong></div>
  </div>
</footer>

<div class="bottom-bar" style="position:absolute;left:0;top:2229px;width:1200px">Copyright &copy; 2014 &nbsp;Brookvale Tech &nbsp;All rights reserved.</div>

</body>
</html>
```